Chorus of the Pacific Presents

Show name:
Bloom Melody Revue
Location:
Wrenfield High School
4218 Larkmoor Ln, Fernbrook Heights, CA 95999
Times: 2 p.m. & 7 p.m.
Special Guests:
Hold Chord
Harbor Quartet
Brightwater Five
Ticket Prices:
VIP $35.00
General $25.00
Student $15.00

```html
<!DOCTYPE html>
<html lang="en">
<head>
<meta charset="utf-8">
<title>Bloom Melody Revue — Chorus of the Pacific</title>
<link rel="stylesheet" href="https://fonts.googleapis.com/css2?family=Alegreya+Sans:wght@400;500;800&display=swap">
<style>
  :root {
    --navy: #1f3357;
    --coral: #e9604a;
    --pill: #6e8b97;
    --white: #ffffff;
    --wash-pink: #f5a0b4;
    --wash-peach: #fbd3b0;
    --wash-yellow: #fbeeb5;
    --wash-green: #d9ecc0;
    --flower-red: #ef6a4c;
    --flower-teal: #2f8d8f;
  }
  * { margin: 0; padding: 0; box-sizing: border-box; }
  html, body { width: 902px; height: 1200px; overflow: hidden; background: #f4f4f2; }
  .poster {
    position: relative; width: 902px; height: 1200px; overflow: hidden;
    font-family: "Alegreya Sans", sans-serif;
    background:
      radial-gradient(ellipse 420px 360px at 60px 140px, var(--wash-pink), transparent 75%),
      radial-gradient(ellipse 360px 320px at 90px 520px, var(--wash-peach), transparent 75%),
      radial-gradient(ellipse 300px 260px at 160px 470px, var(--wash-yellow), transparent 75%),
      radial-gradient(ellipse 380px 420px at 860px 360px, var(--wash-green), transparent 75%),
      radial-gradient(ellipse 320px 260px at 560px 60px, #f9d9e0, transparent 75%),
      #fdfcf8;
  }
  .art { position: absolute; }
  .art--line-florals {
    left: 0; top: 0; width: 902px; height: 360px;
    background: radial-gradient(ellipse 60% 70% at 50% 0%, rgba(92,66,104,0.16), transparent 80%);
  }
  .art--notes-left {
    left: 0; top: 700px; width: 190px; height: 420px;
    background: radial-gradient(ellipse at 40% 50%, rgba(185,220,160,0.45), transparent 70%);
  }
  .art--notes-right {
    right: 0; top: 580px; width: 200px; height: 520px;
    background: radial-gradient(ellipse at 60% 50%, rgba(185,220,160,0.5), transparent 70%);
  }
  .art--flowers-left {
    left: 0; top: 1080px; width: 320px; height: 120px;
    background: linear-gradient(100deg, var(--flower-teal) 0%, var(--flower-red) 35%, #f6b24a 70%, transparent 100%);
    opacity: 0.85;
    border-top-right-radius: 120px 80px;
  }
  .art--flowers-right {
    right: 0; top: 1090px; width: 300px; height: 110px;
    background: linear-gradient(260deg, var(--flower-red) 0%, var(--flower-red) 30%, #f6b24a 65%, transparent 100%);
    opacity: 0.85;
    border-top-left-radius: 120px 80px;
  }
  .panel { position: absolute; left: 190px; top: 70px; width: 528px; height: 1063px; }
  .panel__frame { position: absolute; inset: 0; }
  .panel__content { position: absolute; inset: 0; text-align: center; }
  .row { position: absolute; left: 0; right: 0; text-align: center; }
  .presenter { top: 114px; font-size: 34px; font-weight: 400; line-height: 47px; color: var(--navy); letter-spacing: 0.5px; }
  .show-title { top: 240px; font-size: 62px; font-weight: 800; line-height: 76px; color: var(--navy); letter-spacing: 0.5px; }
  .divider { position: absolute; left: 40px; width: 448px; height: 12px; }
  .label { height: 34px; }
  .label svg { position: absolute; left: 0; top: 0; }
  .label span {
    position: relative; display: inline-block; height: 34px; line-height: 34px;
    padding: 0 20px; border-radius: 17px; background: var(--pill);
    color: var(--white); font-size: 24px; font-weight: 500; letter-spacing: 0.3px;
  }
  .details { font-size: 23px; font-weight: 500; line-height: 31px; color: var(--coral); }
  .details--prices { font-size: 25px; line-height: 33.5px; }
</style>
</head>
<body>
<main class="poster">
  <div class="art art--line-florals" role="img" aria-label="Hand-drawn line-art flowers, berries and leaves across the top"></div>
  <div class="art art--notes-left" role="img" aria-label="Faint green music notes and staff lines"></div>
  <div class="art art--notes-right" role="img" aria-label="Faint green music notes and staff lines"></div>
  <div class="art art--flowers-left" role="img" aria-label="Coral, teal and yellow illustrated flowers"></div>
  <div class="art art--flowers-right" role="img" aria-label="Coral and yellow illustrated flowers"></div>

  <section class="panel">
    <svg class="panel__frame" width="528" height="1063" viewBox="0 0 528 1063">
      <path d="M4 62 Q34 62 44 30 Q264 -18 484 30 Q494 62 524 62 V1001 Q494 1001 484 1033 Q264 1081 44 1033 Q34 1001 4 1001 Z"
            fill="#ffffff" stroke="#1f3357" stroke-width="6"/>
      <path d="M18 76 Q46 74 56 46 Q264 2 472 46 Q482 74 510 76 V987 Q482 989 472 1017 Q264 1061 56 1017 Q46 989 18 987 Z"
            fill="none" stroke="#1f3357" stroke-width="3" stroke-linecap="round" stroke-dasharray="0 9"/>
    </svg>

    <div class="panel__content">
      <h2 class="row presenter">CHORUS OF THE PACIFIC<br>PRESENTS</h2>

      <svg class="divider" style="top:216px" viewBox="0 0 448 12"><line x1="6" y1="6" x2="442" y2="6" stroke="#1f3357" stroke-width="1.5"/><circle cx="6" cy="6" r="3" fill="#1f3357"/><circle cx="442" cy="6" r="3" fill="#1f3357"/></svg>

      <h1 class="row show-title">BLOOM MELODY<br>REVUE</h1>

      <svg class="divider" style="top:408px" viewBox="0 0 448 12"><line x1="6" y1="6" x2="442" y2="6" stroke="#1f3357" stroke-width="1.5"/><circle cx="6" cy="6" r="3" fill="#1f3357"/><circle cx="442" cy="6" r="3" fill="#1f3357"/></svg>

      <div class="row label" style="top:431px">
        <svg width="528" height="34"><line x1="150" y1="17" x2="378" y2="17" stroke="#6e8b97" stroke-width="2"/><circle cx="150" cy="13" r="4" fill="none" stroke="#6e8b97" stroke-width="2"/><circle cx="378" cy="13" r="4" fill="none" stroke="#6e8b97" stroke-width="2"/></svg>
        <span>LOCATION:</span>
      </div>
      <p class="row details" style="top:479px">Wrenfield High School<br>4218 Larkmoor Ln, Fernbrook Heights,<br>CA 95999</p>

      <div class="row label" style="top:593px">
        <svg width="528" height="34"><line x1="170" y1="17" x2="358" y2="17" stroke="#6e8b97" stroke-width="2"/><circle cx="170" cy="13" r="4" fill="none" stroke="#6e8b97" stroke-width="2"/><circle cx="358" cy="13" r="4" fill="none" stroke="#6e8b97" stroke-width="2"/></svg>
        <span>TIMES:</span>
      </div>
      <p class="row details" style="top:641px">2 p.m. &amp; 7 p.m.</p>

      <div class="row label" style="top:696px">
        <svg width="528" height="34"><line x1="120" y1="17" x2="408" y2="17" stroke="#6e8b97" stroke-width="2"/><circle cx="120" cy="13" r="4" fill="none" stroke="#6e8b97" stroke-width="2"/><circle cx="408" cy="13" r="4" fill="none" stroke="#6e8b97" stroke-width="2"/></svg>
        <span>SPECIAL GUESTS:</span>
      </div>
      <p class="row details" style="top:747px">Hold Chord<br>Harbor Quartet<br>Brightwater Five</p>

      <div class="row label" style="top:863px">
        <svg width="528" height="34"><line x1="132" y1="17" x2="396" y2="17" stroke="#6e8b97" stroke-width="2"/><circle cx="132" cy="13" r="4" fill="none" stroke="#6e8b97" stroke-width="2"/><circle cx="396" cy="13" r="4" fill="none" stroke="#6e8b97" stroke-width="2"/></svg>
        <span>TICKET PRICES:</span>
      </div>
      <p class="row details details--prices" style="top:915px">VIP $35.00<br>General $25.00<br>Student $15.00</p>
    </div>
  </section>
</main>
</body>
</html>
```